Aquatic View

We need a web design for a new window cleaning company name Bright Pane Services. We are located in Grand Cayman, Cayman Islands. We are a small company, a team of husband and wife. Our services include residencial interior and exterior window cleaning and commercial. Extra services such as ceiling fans cleaning, mirrors, high dusting. Home cleaning services. Power washing. Explaining the service. We want a modern, beachy style with aquatic colors. We want to use our domain name "brightpaneservices.ky". We want to portray a clean, modern and professional design.

Target Market(s)

Big Home owners

Industry/Entity Type

Cleaning Service

Contact Information for Business Card

Company Name: Bright Pane Services
Name: Gerald Thornbury owner/manager
Phone: 345-9418372
Email: gerald@brightpaneservices.ky
Website: brightpaneservices.ky
Address: P.O.Box 2846 GT, George Town, Grand Cayman KY1-1304 Cayman Islands

Number of Pages Required

2 page

Font styles to use
Sans Serif

Colors
0592cd
0455a3
33a6d7
85cae6
cadf82
abd036
fbf289

Requirements
Nice to have
• Pictures of an ocean view and palm trees from clear windows.
• https://quotrelvane.com/estimately/
• Use the above for "free estimate".

```html
<!DOCTYPE html>
<html lang="en">
<head>
<meta charset="utf-8">
<title>Bright Pane Services</title>
<link href="https://fonts.googleapis.com/css2?family=Lato:wght@400;700&family=Poppins:wght@500;600&family=Open+Sans:wght@600;700&display=swap" rel="stylesheet">
<style>
:root{
  --blue:#0592cd;
  --navy:#0455a3;
  --ink:#2b2b2b;
  --text:#3a3a3a;
  --rule:#cfcfcf;
  --footer:#ececec;
  --caption:rgba(90,90,90,.82);
}
*{box-sizing:border-box;margin:0;padding:0}
html,body{width:966px;height:1200px;overflow:hidden;background:#fff}
body{position:relative;font-family:"Lato",sans-serif;color:var(--text)}
.abs{position:absolute}
.topbar{left:0;top:0;width:966px;height:32px;background:linear-gradient(#0a6fc0,#0592cd)}
.brand{left:90px;top:38px;display:flex;align-items:center;gap:8px;font-weight:700;font-size:17px;color:var(--navy)}
.brand-dot{width:14px;height:14px;border-radius:50%;background:var(--blue)}
.nav{left:574px;top:50px;display:flex;font-family:"Open Sans",sans-serif;font-weight:700;font-size:13px}
.nav a{color:var(--navy);text-decoration:none;height:28px;line-height:28px;padding:0 9px;margin-right:15px}
.nav a.active{background:var(--blue);color:#fff}
.hero{left:0;top:80px;width:966px;height:424px;
  background:linear-gradient(105deg,#f7f7f6 0%,#ecebe8 30%,#e3ddd2 52%,#e8dca6 64%,#c9d3dc 80%,#7fa8d2 100%)}
.hero-caption{left:0;top:457px;width:966px;height:47px;background:var(--caption);color:#fff;text-align:center;font-family:"Open Sans",sans-serif;font-weight:700;font-size:22px;line-height:47px;letter-spacing:.2px}
.arrow{top:218px;width:32px;height:32px}
h1.welcome{left:80px;top:538px;font-family:"Poppins",sans-serif;font-weight:600;font-size:24px;color:var(--ink)}
.accent{color:var(--navy)}
.welcome-rule{left:80px;top:582px;width:511px;height:1px;background:var(--rule)}
.lead{left:81px;top:594px;font-size:14.5px;font-weight:700;color:var(--ink)}
.lead .accent{font-weight:400}
.intro{left:81px;top:627px;width:514px;font-size:12.6px;line-height:19.5px}
.btn{background:var(--blue);color:#fff;text-align:center;font-size:11.5px;font-weight:700}
.read-more{left:80px;top:738px;width:83px;height:27px;line-height:27px}
.inquiry{left:611px;top:555px;width:275px;height:218px;border:1px solid #d6d6d6}
.inquiry-tab{left:661px;top:544px;width:197px;height:34px}
.field{left:630px;width:243px;height:27px;background:linear-gradient(#e6e6e6,#f7f7f7);border:1px solid #d2d2d2;border-radius:2px;font-size:11.5px;color:#333;padding:6px 0 0 6px}
.field b{color:#e0262b;font-weight:400}
.submit{left:631px;top:738px;width:89px;height:27px;line-height:27px;font-weight:400;font-size:13px}
h2.services{left:0;top:812px;width:966px;text-align:center;font-family:"Poppins",sans-serif;font-weight:600;font-size:26px;color:var(--ink)}
.services-rule{left:189px;top:863px;width:587px;height:1px;background:var(--rule)}
.services-mark{left:463px;top:862px;width:40px;height:3px;background:var(--blue)}
.services-intro{left:0;top:880px;width:966px;text-align:center;font-size:15px}
.card{top:919px;width:245px;height:169px}
.card-photo{width:245px;height:134px}
.card-label{width:245px;height:35px;background:var(--blue);color:#fff;font-family:"Poppins",sans-serif;font-weight:600;font-size:17px;line-height:36px;padding-left:10px}
.footer-rule{left:0;top:1127px;width:966px;height:2px;background:var(--blue)}
.footer{left:0;top:1129px;width:966px;height:71px;background:var(--footer)}
.footer-nav{left:77px;top:1155px;font-size:12px;color:#333;word-spacing:1px}
.footer-nav span{margin:0 10px}
.footer-brand{left:0;top:1154px;width:966px;text-align:center;font-size:13px;font-weight:700;color:#555}
.copyright{right:85px;top:1156px;font-size:11.5px;color:#333}
</style>
</head>
<body>
<div class="abs topbar"></div>
<div class="abs brand"><span class="brand-dot"></span>Bright Pane Services</div>
<nav class="abs nav"><a class="active">HOME</a><a>ABOUT</a><a>SERVICES</a><a>CONTACT</a></nav>

<div class="abs hero" role="img" aria-label="Photo of a cleaner in yellow gloves wiping a bright white kitchen counter beside a blue bucket of cleaning supplies"></div>
<div class="abs hero-caption">WE ARE RESIDENTIAL, COMMERCIAL CLEANING SERVICE FIRM</div>
<svg class="abs arrow" style="left:25px" viewBox="0 0 32 32"><circle cx="16" cy="16" r="15" fill="#f4f4f4" stroke="#bbb" stroke-width="2"/><path d="M18 10l-6 6 6 6" fill="none" stroke="#333" stroke-width="3"/></svg>
<svg class="abs arrow" style="left:908px" viewBox="0 0 32 32"><circle cx="16" cy="16" r="15" fill="#f4f4f4" stroke="#bbb" stroke-width="2"/><path d="M14 10l6 6-6 6" fill="none" stroke="#333" stroke-width="3"/></svg>

<h1 class="abs welcome">Welcome To <span class="accent">Bright Pane Services</span></h1>
<div class="abs welcome-rule"></div>
<p class="abs lead"><span class="accent">Bright Pane Services</span> dolor sit amet, consectetuer adipiscing elit, sed dia</p>
<p class="abs intro">Lorem ipsum dolor sit amet, consectetuer adipiscing elit, sed diam nonummy nibh euismod tincidunt ut laoreet dolore magna aliquam erat volutpat. Ut wisi enim ad minim veniam, quis nostrud exerci tation ullamcorper suscipit lobortis nisl ut aliquip ex ea commodo consequat. Duis autem vel eum iriure dolor in hendrerit in vulputate velit.</p>
<div class="abs btn read-more">READ MORE</div>

<div class="abs inquiry"></div>
<svg class="abs inquiry-tab" viewBox="0 0 197 34">
  <path d="M0 10L7 0V10Z M197 10L190 0V10Z" fill="#0455a3"/>
  <rect x="7" y="0" width="183" height="34" fill="#0592cd"/>
  <text x="98.5" y="23" text-anchor="middle" fill="#fff" font-family="Open Sans, sans-serif" font-weight="700" font-size="15">QUICK INQUIRY</text>
</svg>
<div class="abs field" style="top:588px">First Name <b>*</b></div>
<div class="abs field" style="top:621px">Last Name <b>*</b></div>
<div class="abs field" style="top:654px">Email <b>*</b></div>
<div class="abs field" style="top:688px;height:44px">Address<b>*</b></div>
<div class="abs btn submit">SUBMIT</div>

<h2 class="abs services">Our <span class="accent">Services</span></h2>
<div class="abs services-rule"></div>
<div class="abs services-mark"></div>
<p class="abs services-intro">Lorem ipsum dolor sit amet, consectetuer adipiscing elit, sed diam nonummy nibh euismod tincidunt ut</p>

<div class="abs card" style="left:79px">
  <div class="card-photo" role="img" aria-label="Photo of cleaners in navy overalls washing windows in a home kitchen" style="background:linear-gradient(100deg,#e7ebee 0%,#a9b6c9 25%,#d9d3c8 50%,#b48a66 72%,#e1dcd6 100%)"></div>
  <div class="card-label">Residential</div>
</div>
<div class="abs card" style="left:360px">
  <div class="card-photo" role="img" aria-label="Photo of workers mopping a tiled office lobby with yellow caution signs" style="background:linear-gradient(180deg,#d8d6d0 0%,#b68b62 40%,#cfc7bb 65%,#e3ddd4 100%)"></div>
  <div class="card-label">Commercial</div>
</div>
<div class="abs card" style="left:641px">
  <div class="card-photo" role="img" aria-label="Photo of a worker in a hard hat cleaning tall glass office windows" style="background:linear-gradient(90deg,#5d5d60 0%,#8c8e92 18%,#d2d6db 40%,#eceef0 100%)"></div>
  <div class="card-label">Extra Services</div>
</div>

<div class="abs footer-rule"></div>
<div class="abs footer"></div>
<div class="abs footer-nav">HOME<span>|</span>ABOUT<span>|</span>SERVICES<span>|</span>CONTACT</div>
<div class="abs footer-brand">Bright Pane Services</div>
<div class="abs copyright">© 2015 Bright Pane Services . All Rights Reserved</div>
</body>
</html>
```